Brightwell Polar Systems Inc.
Business Card, Letter Head, Fax Cover, evelope and T-shirt
Bright & Fun-filled
Dorian Kestle
342 Harrowgate Ave
Bronx, NY, 10474
dkestle@bpsyst.example
www.Bpsyst.example
ill be using a clear plastic card, but also lets have the background as black.
Heating
Air Condition
Ventilation
Duct Work
Refrigeration
Solar, Geothermal
Design, Fabrication & Installation
Sales, Service & Repair

```html
<!DOCTYPE html>
<html lang="en">
<head>
<meta charset="utf-8">
<title>Brightwell Polar Systems Inc. — Stationery</title>
<link href="https://fonts.googleapis.com/css2?family=Open+Sans:wght@400;700&display=swap" rel="stylesheet">
<style>
  :root {
    --bg: #ece4d6;
    --paper: #ffffff;
    --green: #4f9b2c;
    --green-light: #9fd15a;
    --orange: #e8781c;
    --red-orange: #c9401a;
    --ink: #555555;
    --muted: #9a9a9a;
    --faint: #f4e6d4;
  }
  * { box-sizing: border-box; margin: 0; padding: 0; }
  html, body { width: 1200px; height: 329px; overflow: hidden; }
  body {
    position: relative;
    background: var(--bg);
    font-family: "Open Sans", Arial, sans-serif;
    color: var(--ink);
  }
  .piece { position: absolute; background: var(--paper); box-shadow: 0 1px 4px rgba(0,0,0,.25); overflow: hidden; }

  .logo { display: flex; align-items: center; gap: 3px; }
  .logo-dot { width: 9px; height: 9px; border-radius: 50%; background: var(--orange); flex: none; }
  .logo-name { font-weight: 700; color: var(--green); font-size: 5px; line-height: 1.1; text-transform: uppercase; }

  /* brand strip */
  .brand-strip { position: absolute; left: 4px; top: 10px; width: 52px; height: 310px; }
  .brand-strip .vertical-name {
    position: absolute; left: 8px; top: 5px; height: 240px;
    writing-mode: vertical-rl; transform: rotate(180deg);
    font-weight: 700; font-size: 17px; color: var(--green); letter-spacing: 1px; text-transform: uppercase; text-align: center;
  }
  .brand-strip .brand-dot { position: absolute; left: 6px; bottom: 10px; width: 40px; height: 40px; border-radius: 50%; background: var(--orange); }

  /* business cards */
  .card { width: 148px; height: 104px; background: linear-gradient(90deg, #f7efe2, #fbf7f0); }
  .card::before { content: ""; position: absolute; left: 0; top: 0; bottom: 0; width: 7px; background: linear-gradient(var(--green-light), var(--green)); }
  .card .logo { position: absolute; left: 14px; top: 10px; }
  .card .contact { position: absolute; left: 60px; top: 38px; font-size: 4px; line-height: 1.5; }
  .card .person { font-weight: 700; color: var(--green); font-size: 5px; }

  /* letterhead */
  .letterhead { width: 158px; height: 290px; top: 18px; }
  .letterhead::before { content: ""; position: absolute; left: 8px; top: 8px; width: 2px; height: 80px; background: var(--green); }
  .letterhead .logo { position: absolute; left: 14px; top: 10px; }
  .letterhead .contact { position: absolute; right: 12px; top: 10px; font-size: 3.5px; line-height: 1.5; color: var(--muted); text-align: right; }
  .letterhead .watermark { position: absolute; left: 34px; top: 100px; width: 92px; height: 92px; border-radius: 50%; background: var(--faint); }
  .letterhead .footer { position: absolute; left: 0; right: 0; bottom: 10px; font-size: 3.5px; text-align: center; color: var(--muted); }

  /* slips */
  .slip { width: 214px; }
  .slip .logo { position: absolute; left: 14px; top: 10px; }
  .slip::before { content: ""; position: absolute; left: 8px; top: 8px; width: 2px; height: 40px; background: var(--green); }
  .slip .watermark { position: absolute; left: 72px; width: 70px; height: 70px; border-radius: 50%; background: var(--faint); }
  .slip .footer { position: absolute; left: 0; right: 0; bottom: 6px; font-size: 3.5px; text-align: center; color: var(--muted); }

  /* envelopes */
  .envelope { width: 264px; left: 838px; }
  .envelope svg { position: absolute; inset: 0; }
  .envelope .logo { position: absolute; left: 50%; transform: translateX(-50%); }
</style>
</head>
<body>

  <div class="brand-strip">
    <div class="vertical-name">Brightwell Polar</div>
    <div class="brand-dot"></div>
  </div>

  <!-- business cards -->
  <div class="piece card" style="left:66px; top:58px;">
    <div class="logo"><span class="logo-dot"></span><span class="logo-name">Brightwell Polar<br>Systems Inc.</span></div>
    <div class="contact">
      <div>342 Harrowgate Ave</div>
      <div>Bronx, NY, 10474</div>
      <div>Tel (718) 555-0142</div>
      <div>www.Bpsyst.example</div>
    </div>
  </div>
  <div class="piece card" style="left:66px; top:176px;">
    <div class="logo"><span class="logo-dot"></span><span class="logo-name">Brightwell Polar<br>Systems Inc.</span></div>
    <div class="contact">
      <div class="person">Dorian Kestle</div>
      <div>President</div>
      <div>Cell (718) 555-0199</div>
      <div>dkestle@bpsyst.example</div>
    </div>
  </div>

  <!-- letterheads -->
  <div class="piece letterhead" style="left:222px;">
    <div class="logo"><span class="logo-dot"></span><span class="logo-name">Brightwell Polar<br>Systems Inc.</span></div>
    <div class="contact"><div>Tel (718) 555-0142</div><div>Fax (718) 555-0143</div><div>www.Bpsyst.example</div></div>
    <div class="watermark" role="img" aria-label="Faint brand circle"></div>
    <div class="footer">342 Harrowgate Ave, Bronx, NY, 10474</div>
  </div>
  <div class="piece letterhead" style="left:392px;">
    <div class="logo"><span class="logo-dot"></span><span class="logo-name">Brightwell Polar<br>Systems Inc.</span></div>
    <div class="watermark" role="img" aria-label="Faint brand circle"></div>
    <div class="footer">342 Harrowgate Ave, Bronx, NY, 10474 · www.Bpsyst.example</div>
  </div>

  <!-- slips -->
  <div class="piece slip" style="left:614px; top:84px; height:120px;">
    <div class="logo"><span class="logo-dot"></span><span class="logo-name">Brightwell Polar<br>Systems Inc.</span></div>
    <div class="watermark" role="img" aria-label="Faint brand circle" style="top:22px;"></div>
    <div class="footer">342 Harrowgate Ave, Bronx, NY, 10474</div>
  </div>
  <div class="piece slip" style="left:614px; top:218px; height:90px;">
    <div class="logo"><span class="logo-dot"></span><span class="logo-name">Brightwell Polar<br>Systems Inc.</span></div>
    <div class="watermark" role="img" aria-label="Faint brand circle" style="top:14px; width:60px; height:60px; left:78px;"></div>
    <div class="footer">www.Bpsyst.example</div>
  </div>

  <!-- envelopes -->
  <div class="piece envelope" style="top:64px; height:72px;">
    <svg width="264" height="72" viewBox="0 0 264 72">
      <defs><linearGradient id="flapWarm" x1="0" y1="0" x2="0" y2="1"><stop offset="0" stop-color="#c9401a"/><stop offset="1" stop-color="#f0a030"/></linearGradient></defs>
      <path d="M0 0 H264 V20 L132 52 L0 20 Z" fill="url(#flapWarm)"/>
    </svg>
    <div class="logo" style="top:36px;"><span class="logo-dot"></span><span class="logo-name">Brightwell Polar</span></div>
  </div>
  <div class="piece envelope" style="top:140px; height:72px;">
    <svg width="264" height="72" viewBox="0 0 264 72">
      <defs><linearGradient id="flapGreen" x1="0" y1="0" x2="0" y2="1"><stop offset="0" stop-color="#4f9b2c"/><stop offset="1" stop-color="#a6d45e"/></linearGradient></defs>
      <path d="M0 0 H264 V14 L132 46 L0 14 Z" fill="url(#flapGreen)"/>
    </svg>
    <div class="logo" style="top:32px;"><span class="logo-dot"></span><span class="logo-name">Brightwell Polar</span></div>
  </div>
  <div class="piece envelope" style="top:216px; height:86px;">
    <svg width="264" height="86" viewBox="0 0 264 86">
      <path d="M0 0 L132 38 L264 0" fill="none" stroke="#d6d6d6" stroke-width="1"/>
      <path d="M0 86 L110 42 M264 86 L154 42" fill="none" stroke="#e2e2e2" stroke-width="1"/>
    </svg>
    <div class="logo" style="top:30px;"><span class="logo-dot"></span><span class="logo-name">Brightwell Polar</span></div>
  </div>

</body>
</html>
```